Top International Talent Management Needs creative business card design

We manage actors careers and book them liaising and promoting their profiles internationally through Casting Directors, Producers, Directors, Publicists etc. We need clearly visable contact details but with a design that reflects our status and creativity of TV, Feature Film industry. Our logo is attached and needs to relate and our website is www.marrowlanepeople.com
No flame designs please but please incorporate logo colours.

Target Market(s)

Clients

Industry/Entity Type

Film Production

Contact Information for Business Card

Director Rosalind Tebbett
Suite F, Building 4, Harrowgate Sound Stages, Tullick Vale, Sydney, NSW 2021

Font styles to use
Sans Serif

Colors
ec1f27

Requirements
Nice to have
• Colours should relate to logo attached and type can relate again to type in the logo design.
Should not have
• No Flames designs and best to be not too obvious with the film designs eiither. Needs to be more creative and modern

```html
<!DOCTYPE html>
<html lang="en">
<head>
<meta charset="utf-8">
<title>Marrow Lane People – Business Card</title>
<link rel="stylesheet" href="https://fonts.googleapis.com/css2?family=Open+Sans:wght@400;600;700&display=swap">
<style>
  :root {
    --brand-red: #ec1f27;
    --brand-red-deep: #c8141b;
    --ink: #1d1d1d;
    --ink-soft: #3a3a3a;
    --paper: #ffffff;
    --stage: #e9e7e4;
    --silver: #f1f1f1;
    --grey-art: #b9b9b9;
  }
  * { box-sizing: border-box; margin: 0; padding: 0; }
  html, body { width: 1200px; height: 784px; overflow: hidden; }
  body {
    background: var(--stage);
    font-family: "Open Sans", Arial, sans-serif;
    display: flex;
    align-items: center;
    justify-content: center;
    gap: 40px;
  }
  .card {
    position: relative;
    width: 560px;
    height: 320px;
    overflow: hidden;
    box-shadow: 0 2px 10px rgba(0,0,0,0.12);
  }

  /* Front */
  .card--front {
    background: linear-gradient(135deg, var(--brand-red) 0%, var(--brand-red-deep) 100%);
  }
  .front-art {
    position: absolute;
    left: 0; top: 0;
    width: 100%; height: 100%;
    background:
      radial-gradient(circle at 22% 55%, rgba(255,255,255,0.10) 0 90px, transparent 92px),
      linear-gradient(100deg, transparent 45%, rgba(0,0,0,0.08) 55%, transparent 75%);
  }
  .front-logo {
    position: absolute;
    left: 110px;
    top: 118px;
    color: var(--silver);
    font-weight: 700;
    letter-spacing: 2px;
    line-height: 1;
  }
  .front-logo .logo-name { font-size: 48px; }
  .front-logo .logo-sub { font-size: 18px; letter-spacing: 1px; margin-top: 6px; text-align: right; }

  /* Back */
  .card--back { background: var(--paper); }
  .back-logo {
    position: absolute;
    left: 38px;
    top: 58px;
    color: var(--brand-red);
    font-weight: 700;
    letter-spacing: 2px;
    line-height: 1;
  }
  .back-logo .logo-name { font-size: 40px; }
  .back-logo .logo-sub { font-size: 15px; letter-spacing: 1px; margin-top: 5px; text-align: right; }
  .back-art {
    position: absolute;
    right: 0;
    top: 40px;
    width: 170px;
    height: 190px;
    background: radial-gradient(ellipse at 55% 50%, rgba(150,150,150,0.55) 0%, rgba(200,200,200,0.35) 50%, rgba(255,255,255,0) 75%);
  }
  .social {
    position: absolute;
    right: 40px;
    top: 150px;
    display: flex;
    gap: 4px;
  }
  .social span {
    width: 18px; height: 18px;
    background: var(--brand-red);
    border-radius: 2px;
  }
  .person {
    position: absolute;
    left: 38px;
    top: 150px;
  }
  .person-name { color: var(--brand-red); font-size: 18px; font-weight: 600; }
  .person-role { color: var(--ink); font-size: 12px; margin-top: 1px; }
  .contact {
    position: absolute;
    left: 38px;
    top: 205px;
    list-style: none;
    color: var(--ink-soft);
    font-size: 13.5px;
    line-height: 18px;
  }
  .contact li { display: flex; align-items: flex-start; gap: 7px; }
  .contact svg { width: 13px; height: 13px; flex: none; margin-top: 2px; fill: var(--brand-red); }
</style>
</head>
<body>

  <section class="card card--front" aria-label="Card front">
    <div class="front-art" role="img" aria-label="Faint film reel and film strip artwork in darker red tones"></div>
    <div class="front-logo">
      <div class="logo-name">MARROW LANE</div>
      <div class="logo-sub">People</div>
    </div>
  </section>

  <section class="card card--back" aria-label="Card back">
    <div class="back-logo">
      <div class="logo-name">MARROW LANE</div>
      <div class="logo-sub">People</div>
    </div>
    <div class="back-art" role="img" aria-label="Grey illustration of a film camera, clapperboard and film reels"></div>
    <div class="social" aria-label="Social links">
      <span></span><span></span>
    </div>

    <div class="person">
      <div class="person-name">Rosalind Tebbett</div>
      <div class="person-role">Director</div>
    </div>

    <ul class="contact">
      <li>
        <svg viewBox="0 0 16 16" aria-hidden="true"><path d="M3.5 1l2.5 3-1.5 1.8c.8 1.8 2.2 3.2 4 4l1.8-1.5 3 2.5-1.3 2.5C7 13 3 9 1 2.8z"/></svg>
        <span>+61(0)491570156</span>
      </li>
      <li>
        <svg viewBox="0 0 16 16" aria-hidden="true"><path d="M1 3h14v10H1z M2 4.2v.5L8 9l6-4.3v-.5z" fill-rule="evenodd"/></svg>
        <span>talent@marrowlanepeople.com</span>
      </li>
      <li>
        <svg viewBox="0 0 16 16" aria-hidden="true"><path fill-rule="evenodd" d="M8 1a7 7 0 110 14A7 7 0 018 1zm0 1.5c-.9 1-1.5 2.8-1.6 4.7h3.2C9.5 5.3 8.9 3.5 8 2.5zM2.6 7.2h2.4c.1-1.7.5-3.2 1.1-4.3a5.6 5.6 0 00-3.5 4.3zm8.4 0h2.4a5.6 5.6 0 00-3.5-4.3c.6 1.1 1 2.6 1.1 4.3zM2.6 8.8a5.6 5.6 0 003.5 4.3c-.6-1.1-1-2.6-1.1-4.3zm3.8 0c.1 1.9.7 3.7 1.6 4.7.9-1 1.5-2.8 1.6-4.7zm4.6 0c-.1 1.7-.5 3.2-1.1 4.3a5.6 5.6 0 003.5-4.3z"/></svg>
        <span>www.marrowlanepeople.com</span>
      </li>
      <li>
        <svg viewBox="0 0 16 16" aria-hidden="true"><path d="M8 1.5L1 8h2v6.5h4v-4h2v4h4V8h2z"/></svg>
        <span>Suite F, Building 4, Harrowgate Sound Stages,<br>Tullick Vale, Sydney, NSW 2021</span>
      </li>
    </ul>
  </section>

</body>
</html>
```